card design for engineering consultancy

engineering drafting and project management company the provides drafting services for.
Electrical, Hydraulic, Mechanical, and Civil services
The company is called Q7R Services and logo is as attached
Information on card should be.
1. Logo
2.website : Q7RServices.example
3. email : info@Q7RServices.example
4. Phone: (+61) 400512836
5. Motto: Design - Document - Develop - Deliver

this card should be basically used for business identification only

Target Market(s)

electricians plumbers air conditioning installers and civil contractors

Industry/Entity Type

engineering, drafting, electrical, plumbing, airconditioning, civil

Contact Information for Business Card

1. Logo 2.website : Q7RServices.example 3. email : info@Q7RServices.example 4. Phone: (+61) 400512836 5. Motto: Design - Document - Develop - Deliver

Font styles to use
Serif

Requirements
Must have
• logo
Nice to have
• something inovative and different that makes it stand out from being just another business card

```html
<!DOCTYPE html>
<html lang="en">
<head>
<meta charset="utf-8">
<title>Q7R Services – Business Card</title>
<link rel="stylesheet" href="https://fonts.googleapis.com/css2?family=Tinos:wght@400;700&display=swap">
<style>
  :root {
    --canvas: #ffffff;
    --card: #fefefe;
    --card-edge: #c9c9c9;
    --brand-grey: #545050;
    --ink: #111111;
    --icon-bg: #0d0d0d;
    --icon-fg: #ffffff;
  }
  * { margin: 0; padding: 0; box-sizing: border-box; }
  html, body {
    width: 1200px; height: 1000px; overflow: hidden;
    background: var(--canvas);
    font-family: "Tinos", "Times New Roman", serif;
    color: var(--ink);
  }
  .card {
    position: absolute;
    left: 223px; width: 754px; height: 432px;
    background: var(--card);
    border: 1px solid var(--card-edge);
  }
  .card--front { top: 25px; }
  .card--back { top: 543px; }

  .brand-name {
    position: absolute;
    color: var(--brand-grey);
    font-weight: 700;
    white-space: nowrap;
    letter-spacing: 1px;
  }
  .card--front .brand-name {
    left: 0; right: 0; top: 140px;
    text-align: center;
    font-size: 60px;
  }
  .card--back .brand-name {
    left: 54px; top: 70px;
    font-size: 40px;
  }

  .motto {
    position: absolute;
    left: 0; right: 0; top: 302px;
    text-align: center;
    font-size: 23px;
  }

  .contact-list {
    position: absolute;
    left: 410px; top: 238px;
    list-style: none;
  }
  .contact-item {
    display: flex; align-items: center;
    height: 28px; margin-bottom: 25px;
    font-size: 23px;
  }
  .contact-icon {
    width: 28px; height: 28px; flex: none;
    margin-right: 25px;
  }
</style>
</head>
<body>
  <section class="card card--front" aria-label="Card front">
    <div class="brand-name">Q7R Services</div>
    <p class="motto">Design - Document - Develop - Deliver</p>
  </section>

  <section class="card card--back" aria-label="Card back">
    <div class="brand-name">Q7R Services</div>
    <ul class="contact-list">
      <li class="contact-item">
        <svg class="contact-icon" viewBox="0 0 28 28" aria-hidden="true">
          <circle cx="14" cy="14" r="13" fill="var(--icon-bg)"/>
          <path d="M10 8.5c.6-.5 1.3-.4 1.7.2l1.2 1.8c.3.5.2 1.1-.2 1.5l-.8.7c.6 1.4 1.8 2.7 3.3 3.4l.7-.8c.4-.4 1-.5 1.5-.2l1.8 1.1c.6.4.7 1.2.2 1.7l-.9 1c-.7.7-1.8.9-2.8.5-3.2-1.3-5.6-3.8-6.9-6.9-.4-1-.2-2.1.5-2.8z" fill="var(--icon-fg)"/>
        </svg>
        <span>Q7RServices.example</span>
      </li>
      <li class="contact-item">
        <svg class="contact-icon" viewBox="0 0 28 28" aria-hidden="true">
          <circle cx="14" cy="14" r="13" fill="var(--icon-bg)"/>
          <rect x="7.5" y="9.5" width="13" height="9" rx="1" fill="none" stroke="var(--icon-fg)" stroke-width="1.3"/>
          <path d="M8 10l6 4.6 6-4.6" fill="none" stroke="var(--icon-fg)" stroke-width="1.3"/>
        </svg>
        <span>(+61) 400512836</span>
      </li>
      <li class="contact-item">
        <svg class="contact-icon" viewBox="0 0 28 28" aria-hidden="true">
          <circle cx="14" cy="14" r="13" fill="var(--icon-bg)"/>
          <g fill="none" stroke="var(--icon-fg)" stroke-width="1.2">
            <circle cx="14" cy="14" r="7"/>
            <ellipse cx="14" cy="14" rx="3" ry="7"/>
            <path d="M7 14h14M8 10.5h12M8 17.5h12"/>
          </g>
        </svg>
        <span>info@Q7RServices.example</span>
      </li>
    </ul>
  </section>
</body>
</html>
```